Create the artwork for Velvetharbor's debut album, 'Where Rivers Bend Slowly'!

We are a cinematic pop/jazz quartet from Oslo/London looking for someone to create the artwork for our debutalbum, 'Where Rivers Bend Slowly'. This is a project we are incredibly proud of, and we are looking for the perfect artwork to complement our music.

We want the artwork to convey the organic feel of our sound, yet be eye-catching with bright colours. Attached are several examples for inspiration. The title of the album, 'Where Rivers Bend Slowly', should be an inspiration for the design in a subtle/abstract way. Think out of the box here, we are not looking for a hundred solar system designs.

You can find an album teaser here for inspiration: https://audiostreamhub.example/velvetharbormusic/album-teaser

This is our webpage: velvetharbormusic.example

Excited to see what you come up with and to work with some brilliant creatives !

Much love,

Velvetharbor
Updates

Everyone, thanks for your effort and great designs! We're discussing right now and will get back to you with feedback and suggested edits very shortly. Thanks for your patience! Much love, Velvetharbor

Requirements
Must have
• Ready-to-print high-res files in standard CD Cover format
• Artwork ready for digital release on tunewave, Songvault, and social media channels
Nice to have
• Would love to have smaller extensions of the artwork (pattern or pieces of art in same theme) to use on webpage/social media channels.

```html
<!DOCTYPE html>
<html lang="en">
<head>
<meta charset="utf-8">
<title>Velvetharbor – Where Rivers Bend Slowly</title>
<link rel="stylesheet" href="https://fonts.googleapis.com/css2?family=Barlow:wght@600;700&display=swap">
<style>
  :root {
    --bg-light: #d4d4d4;
    --bg-dark: #a9a9a9;
    --type: #e2e2e2;
    --tone-blue: #2a1ce0;
    --tone-cyan: #1aa6e0;
    --tone-violet: #8a1fd6;
    --tone-green: #10c060;
  }
  html, body {
    margin: 0;
    padding: 0;
    overflow: hidden;
  }
  .album-cover {
    position: relative;
    width: 1200px;
    height: 1200px;
    overflow: hidden;
    background: linear-gradient(135deg, var(--bg-light) 0%, var(--bg-dark) 100%);
    font-family: "Barlow", "Helvetica Neue", Arial, sans-serif;
  }
  .artwork-area {
    position: absolute;
    left: 394px;
    top: 372px;
    width: 464px;
    height: 472px;
    background: radial-gradient(circle at 50% 50%,
      var(--tone-cyan) 0%,
      var(--tone-blue) 35%,
      var(--tone-violet) 65%,
      var(--tone-green) 100%);
  }
  .cover-titles {
    position: absolute;
    left: 38px;
    top: 1074px;
    margin: 0;
    color: var(--type);
    text-transform: uppercase;
    line-height: 1;
  }
  .artist-name {
    display: block;
    font-weight: 600;
    font-size: 40px;
    letter-spacing: 0.5px;
  }
  .album-title {
    display: block;
    margin-top: -8px;
    font-weight: 700;
    font-size: 56px;
    letter-spacing: 0.5px;
  }
</style>
</head>
<body>
  <main class="album-cover">
    <div class="artwork-area" role="img" aria-label="Abstract folded rainbow starburst artwork radiating from a central point in bright blue, violet, red, yellow and green"></div>
    <h1 class="cover-titles">
      <span class="artist-name">Velvetharbor</span>
      <span class="album-title">Where Rivers Bend Slowly</span>
    </h1>
  </main>
</body>
</html>
```